Dune Power Expo Infographic

We need to have an Infographic designed that displays statistics about the energy sector in Saudi Arabia.

We are an exhibitions organiser but we only want to link it back to the exhibition, Dune Power Expo, by including our logo in the corner under the title 'Created by' (the logo is attached). The rest of the information and design needs to be entirely related to the industry and not the exhibition at all.

The objective of the Infographic is to convey the hard facts about a serious topic in an easy to digest manner. I have attached a word document with a few Infographic designs that we like.

We are using the Infographic for digital designs only so please make sure the Infographic fits onto a web screen easily and there is no need to scroll to see the information but other than that we are relatively flexible on the size.

The content is as follows but please feel free to interpret the content rather than copy word for word:
- Electricity consumption in Saudi Arabia increased sharply during the 1990–2010 period due to rapid economic development. Peak loads reached nearly 24 GW in 2001—25 times their 1975 level-and are expected to approach 60 GW by 2023
- The investment needed to meet this demand may exceed $90 billion. Consequently, there is an urgent need to develop energy conservation policies for sustainable development
- Generation capacity is approximately 55 GW. A looming energy shortage requires Saudi Arabia to increase its capacity. Capacity is planned to be increased to 120 GW by 2020.
- The government has approved the construction of a $300 million facility to turn waste into energy. The facility will process 180 tons of waste per day, producing 6 MW of electricity and 250,000 US gallons (950 m3) of distilled water.
- If energy conservation is successful, demand can be reduced by 5–10%. This is equivalent to 3–6 GW of additional capacity, which represents a possible $1.5–3.0 billion saving over 20 years.
- Saudi Arabia, has said it hopes to generate solar power of up to 41GW by 2032, or 30 per cent of peak power demand. That is almost double the current capacity of Germany, the world’s leading solar power.
- Saudi Arabia will invest in 17 new nuclear reactors in next 20 years.
- Coastal Brine Treatment Authority needs to increase desalinated water supply to 8.5m cubic metres a day by 2025
- Saudi Arabia is building the world’s largest solar-powered desalination plant at Khafji, which will produce 30,000 cubic metres a day of water once it is completed in the next two years. All power and water plants built from 2020 onwards will run on solar energy, NORIV’s Prince Walid said.
- Construction projects worth $75.6bn in Saudi Arabia during 2014, over 10% increase from 2013, $195.4 billion worth of construction planned in Saudi Arabia in the coming three years, and a further over $1 trillion worth of projects planned or under construction

Feel free to post any questions about this project and I will get back to you as soon as possible.

I look forward to seeing your designs!

```html
<!DOCTYPE html>
<html lang="en">
<head>
<meta charset="utf-8">
<title>Energy Sector in Saudi Arabia</title>
<link rel="stylesheet" href="https://fonts.googleapis.com/css2?family=Lora:ital,wght@1,700&family=Source+Sans+3:wght@400;600;700&family=Tinos:wght@400;700&display=swap">
<style>
:root{
  --red:#e0163c;
  --orange:#e8843c;
  --orange-text:#e98a45;
  --blue:#1b9bd7;
  --beige:#f7eddd;
  --white:#ffffff;
  --ink:#231f20;
  --khaki:#9b9379;
  --nuclear:#a59d80;
  --yellow:#f6c40f;
  --water:#5fc4ea;
  --rule:#ffffff;
  --brace:#9a9a9a;
}
*{margin:0;padding:0;box-sizing:border-box}
html,body{width:1200px;height:772px;overflow:hidden;background:var(--beige)}
body{font-family:"Tinos","Times New Roman",serif;color:var(--ink)}
.canvas{position:relative;width:1200px;height:772px;background:var(--beige);overflow:hidden}
.abs{position:absolute}
.header{position:absolute;left:0;top:0;width:1200px;height:139px;background:var(--white)}
.title{position:absolute;left:334px;top:34px;font-family:"Source Sans 3",sans-serif;font-weight:400;font-size:44px;letter-spacing:-0.5px;white-space:nowrap;line-height:1}
.title .red{color:var(--red)}
.title .blue{color:var(--blue)}
.plug{position:absolute;left:288px;top:42px;width:36px;height:40px;background:var(--red);border-radius:4px}
.intro{position:absolute;left:232px;top:105px;width:720px;font-size:11px;line-height:14px;text-align:center}
.brand{position:absolute;left:982px;top:98px;width:190px;text-align:center}
.brand-name{font-family:"Tinos","Times New Roman",serif;font-weight:700;font-size:22px;line-height:26px;color:var(--blue);white-space:nowrap}
.rule{position:absolute;background:var(--rule)}
.gauge{position:absolute;left:39px;top:159px;width:128px;height:90px;background:var(--red);border-radius:64px 64px 0 0}
.peak{position:absolute;font-family:"Lora",serif;font-style:italic;font-weight:700;white-space:nowrap;line-height:1}
.year{position:absolute;top:268px;font-family:"Lora",serif;font-style:italic;font-weight:700;font-size:12px}
.body-text{position:absolute;font-size:11px;line-height:14px}
.justify{text-align:justify;text-align-last:center}
.center{text-align:center}
.callout{position:absolute;background:var(--orange);color:var(--ink)}
.conserve{left:137px;top:427px;width:284px;height:42px;font-size:11px;line-height:14px;display:flex;align-items:center;justify-content:center;text-align:center;padding:0 8px}
.battery{position:absolute;left:79px;top:559px;width:334px;height:88px;background:var(--orange);border-radius:12px}
.battery-nub{position:absolute;left:69px;top:583px;width:12px;height:39px;background:var(--orange);border-radius:4px 0 0 4px}
.battery-core{position:absolute;left:93px;top:572px;width:312px;height:66px;background:var(--white);border-radius:8px}
.cell-now{position:absolute;left:101px;top:574px;width:163px;height:60px;background:var(--yellow);border-radius:4px;text-align:center}
.cell-now .num,.cell-add .num{display:block;font-weight:700;font-size:29px;line-height:32px;margin-top:4px}
.cell-now .lbl,.cell-add .lbl{display:block;font-size:14.5px;line-height:16px}
.cell-add{position:absolute;left:268px;top:574px;width:135px;height:60px;text-align:center}
.big{position:absolute;color:var(--orange-text);white-space:nowrap;line-height:1;text-align:center}
.waste-box{left:516px;top:160px;width:261px;height:61px;text-align:center;padding-top:8px}
.waste-box .small{display:block;font-size:9.5px;line-height:12px}
.waste-box .lead{display:block;font-size:23px;line-height:26px}
.bin{position:absolute;left:514px;top:231px;width:135px;height:168px;background:var(--khaki);border-radius:10px 10px 14px 14px}
.bin-label{position:absolute;left:514px;top:303px;width:135px;text-align:center;color:var(--white);font-weight:700;font-size:26px;line-height:28px}
.bulb{position:absolute;left:716px;top:236px;width:49px;height:74px;background:var(--yellow);border-radius:25px 25px 6px 6px}
.bulb-label{position:absolute;left:716px;top:248px;width:49px;text-align:center;color:var(--white);font-weight:700;font-size:10px}
.tap{position:absolute;left:722px;top:321px;width:32px;height:22px;background:var(--ink);border-radius:3px}
.tap-drop{position:absolute;left:731px;top:347px;width:18px;height:28px;background:var(--water);border-radius:50% 50% 50% 50%/60% 60% 40% 40%}
.tag{position:absolute;font-size:10.5px;white-space:nowrap}
.island{position:absolute;left:639px;top:519px;width:102px;height:91px;background:linear-gradient(180deg,var(--beige) 0%,var(--khaki) 100%);border-radius:50% 50% 8px 8px}
.brine-box{left:516px;top:610px;width:261px;height:60px;text-align:center;padding-top:7px}
.brine-box .lead{display:block;font-size:14.5px;line-height:17px;color:#1f2b3a}
.brine-box .small{display:block;font-size:9.5px;line-height:12px;color:#1f2b3a}
.sun{position:absolute;left:967px;top:233px;width:68px;height:69px;background:var(--yellow);border-radius:50%}
.solar-box{left:889px;top:334px;width:260px;height:129px;padding:6px 10px}
.solar-box .small{display:block;text-align:center;font-size:11px;line-height:13px}
.solar-box .lead{display:block;text-align:center;font-size:16.5px;line-height:19px}
.solar-box .para{display:block;font-size:9.8px;line-height:13px;text-align:justify;text-align-last:center}
</style>
</head>
<body>
<main class="canvas">
  <header class="header">
    <span class="plug" role="img" aria-label="Power plug icon"></span>
    <h1 class="title"><span class="red">Energy Sector</span> <span class="blue">in Saudi Arabia</span></h1>
    <p class="intro">Construction projects below worth $75.6bn in Saudi Arabia during 2014, over 10% increase from 2013, $195.4 billion worth of construction planned<br>in Saudi Arabia in the comingthree years, and a further over $1 trillion worth of projects planned or under construction</p>
    <div class="brand"><span class="brand-name">Dune Power Expo</span></div>
  </header>

  <div class="rule" style="left:475px;top:160px;width:2px;height:604px"></div>
  <div class="rule" style="left:846px;top:160px;width:2px;height:604px"></div>
  <div class="rule" style="left:38px;top:517px;width:432px;height:2px"></div>
  <div class="rule" style="left:476px;top:500px;width:370px;height:2px"></div>
  <div class="rule" style="left:849px;top:476px;width:338px;height:2px"></div>

  <section class="consumption">
    <div class="gauge" role="img" aria-label="Red speedometer gauge with needle pointing high"></div>
    <svg class="abs" style="left:0;top:140px" width="470" height="200" viewBox="0 140 470 200">
      <polygon points="341,152 375,201 307,201" fill="var(--red)"/>
      <rect x="338" y="163" width="6" height="24" fill="var(--white)"/>
      <rect x="338" y="191" width="6" height="6" fill="var(--white)"/>
      <polyline points="137,255 167,225 236,225" fill="none" stroke="var(--ink)" stroke-width="1.2"/>
      <polyline points="300,225 420,225 429,255" fill="none" stroke="var(--ink)" stroke-width="1.2"/>
      <line x1="56" y1="255" x2="429" y2="255" stroke="var(--ink)" stroke-width="3"/>
      <circle cx="56" cy="255" r="5.5" fill="#f0584f"/>
      <circle cx="137" cy="255" r="5.5" fill="#f0584f"/>
      <circle cx="246" cy="255" r="5.5" fill="#f0584f"/>
      <circle cx="429" cy="255" r="5.5" fill="#f0584f"/>
      <path d="M53 296 q0 14 14 14 h78 q9 0 11 11 q2 -11 11 -11 h68 q14 0 14 -14" fill="none" stroke="var(--brace)" stroke-width="1.2"/>
      <path d="M266 296 q0 14 14 14 h58 q9 0 10 11 q1 -11 10 -11 h55 q14 0 14 -14" fill="none" stroke="var(--brace)" stroke-width="1.2"/>
    </svg>
    <span class="peak" style="left:171px;top:203px;font-size:20px">24GW</span>
    <span class="peak" style="left:307px;top:204px;font-size:19px;color:var(--red)">60GW</span>
    <span class="peak" style="left:304px;top:229px;font-size:18px;color:var(--red)">&gt;$90 bilion</span>
    <span class="year" style="left:41px">1990</span>
    <span class="year" style="left:126px">2001</span>
    <span class="year" style="left:225px">2010</span>
    <span class="year" style="left:397px">2032</span>
    <p class="body-text justify" style="left:41px;top:335px;width:201px">Electricity consumption in Saudi Arabia increased sharply during the 1990–2010 period due to rapid economic development.</p>
    <p class="body-text center" style="left:258px;top:336px;width:210px">5 times their&nbsp; 1975 level-and are expected<br>to approach 60 GW by 2032 .<br>The investment needed to meet this<br>demand may exceed $90 billion.</p>
    <svg class="abs" style="left:28px;top:390px" width="102" height="80" viewBox="0 0 102 80">
      <polygon points="51,0 102,80 0,80" fill="var(--red)"/>
      <rect x="47" y="24" width="8" height="32" fill="var(--white)"/>
      <rect x="47" y="62" width="8" height="8" fill="var(--white)"/>
    </svg>
    <p class="callout conserve">Consequently, there is an urgent need to develop energy conservation policies for sustainable development</p>
  </section>

  <section class="capacity">
    <div class="battery-nub"></div>
    <div class="battery"></div>
    <div class="battery-core"></div>
    <div class="cell-now"><span class="num">55 GW</span><span class="lbl">Generation capacity</span></div>
    <div class="cell-add"><span class="num">+ 65GW</span><span class="lbl">Planned to increase</span></div>
    <p class="body-text center" style="left:57px;top:656px;width:400px;font-size:14.5px;line-height:17px">Capacity is planned to be increased to</p>
    <p class="big" style="left:57px;top:677px;width:400px;font-size:37px">120 GW by 2020</p>
  </section>

  <section class="waste">
    <svg class="abs" style="left:590px;top:220px" width="30" height="26" viewBox="0 0 30 26"><polygon points="0,0 30,0 12,24" fill="var(--orange)"/></svg>
    <p class="callout waste-box"><span class="small">The government has approved the construction&nbsp; to turn</span><span class="lead">waste into energy.</span></p>
    <div class="bin" role="img" aria-label="Bin overflowing with waste"></div>
    <p class="bin-label">180<br>tons</p>
    <svg class="abs" style="left:649px;top:300px" width="90" height="100" viewBox="649 300 90 100">
      <polyline points="649,309 740,309" fill="none" stroke="var(--orange)" stroke-width="3"/>
      <polyline points="649,390 686,390 686,326 724,326" fill="none" stroke="var(--orange)" stroke-width="3"/>
    </svg>
    <span class="tag" style="left:669px;top:288px">turn into</span>
    <span class="tag" style="left:645px;top:375px">turn into</span>
    <div class="bulb" role="img" aria-label="Light bulb"></div>
    <span class="bulb-label">6MW</span>
    <div class="tap" role="img" aria-label="Water tap"></div>
    <div class="tap-drop"></div>
    <span class="tag" style="left:727px;top:384px">950 m3</span>
    <p class="body-text center" style="left:517px;top:416px;width:260px;font-size:11px">demand can be reduced by</p>
    <p class="big" style="left:497px;top:428px;width:300px;font-size:31px">5–10% / 3-6GW</p>
    <p class="body-text center" style="left:507px;top:457px;width:280px">which represents a possible $1.5–3.0 billion<br>saving over 20 years.</p>
  </section>

  <section class="brine">
    <div class="island" role="img" aria-label="Palm trees on a small sand island"></div>
    <p class="callout brine-box"><span class="lead">Coastal Brine Treatment Authority</span><span class="small">needs to increase desalinated water supply to 8.5m<br>cubic metres a day by 2025</span></p>
    <svg class="abs" style="left:525px;top:668px" width="255" height="82" viewBox="0 0 255 82" role="img" aria-label="Falling water drops">
      <g fill="var(--water)">
        <path d="M8 0 q10 14 10 22 a10 10 0 0 1 -20 0 q0 -8 10 -22z" transform="translate(6,0)"/>
        <path d="M8 0 q10 14 10 22 a10 10 0 0 1 -20 0 q0 -8 10 -22z" transform="translate(60,-2) scale(1.2)"/>
        <path d="M8 0 q10 14 10 22 a10 10 0 0 1 -20 0 q0 -8 10 -22z" transform="translate(108,2)"/>
        <path d="M8 0 q10 14 10 22 a10 10 0 0 1 -20 0 q0 -8 10 -22z" transform="translate(158,0) scale(1.3)"/>
        <path d="M8 0 q10 14 10 22 a10 10 0 0 1 -20 0 q0 -8 10 -22z" transform="translate(206,-2)"/>
        <path d="M8 0 q10 14 10 22 a10 10 0 0 1 -20 0 q0 -8 10 -22z" transform="translate(236,24)"/>
        <path d="M8 0 q10 14 10 22 a10 10 0 0 1 -20 0 q0 -8 10 -22z" transform="translate(86,44) scale(1.1)"/>
      </g>
    </svg>
  </section>

  <section class="solar">
    <p class="body-text center" style="left:869px;top:159px;width:300px;font-size:11px">We hope the solar power generated to</p>
    <p class="abs" style="left:869px;top:173px;width:300px;text-align:center;white-space:nowrap"><span style="color:var(--orange-text);font-size:27px">41GW / 30%</span> <span style="font-size:11px">&nbsp;by 2032</span></p>
    <p class="body-text center" style="left:869px;top:201px;width:300px">That is almost double the current capacity<br>of Germany, the world’s leading solar power.</p>
    <div class="sun" role="img" aria-label="Shining sun"></div>
    <svg class="abs" style="left:984px;top:314px" width="22" height="21" viewBox="0 0 22 21"><polygon points="11,0 22,21 0,21" fill="var(--orange)"/></svg>
    <div class="callout solar-box">
      <span class="small">Saudi Arabia is building</span>
      <span class="lead">the world’s largest solar powered</span>
      <span class="para">desalination plant at Khafji, which will produce 30,000 cubic metres a day of water once it is completed in the next two years. “All power and water plants built from 2020 onwards will run on solar energy,” NORIV’s Prince Walid said.</span>
    </div>
  </section>

  <section class="nuclear">
    <svg class="abs" style="left:910px;top:498px" width="220" height="170" viewBox="910 498 220 170" role="img" aria-label="Seventeen radiation hazard symbols">
      <g fill="var(--nuclear)">
        <circle cx="934" cy="519" r="18"/><circle cx="977" cy="519" r="18"/><circle cx="1020" cy="519" r="18"/><circle cx="1063" cy="519" r="18"/><circle cx="1106" cy="519" r="18"/>
        <circle cx="934" cy="562" r="18"/><circle cx="977" cy="562" r="18"/><circle cx="1020" cy="562" r="18"/><circle cx="1063" cy="562" r="18"/><circle cx="1106" cy="562" r="18"/>
        <circle cx="934" cy="605" r="18"/><circle cx="977" cy="605" r="18"/><circle cx="1020" cy="605" r="18"/><circle cx="1063" cy="605" r="18"/><circle cx="1106" cy="605" r="18"/>
        <circle cx="994" cy="647" r="18"/><circle cx="1037" cy="647" r="18"/>
      </g>
    </svg>
    <p class="body-text center" style="left:869px;top:675px;width:300px;font-size:14px;line-height:16px">Saudi Arabia will invest in</p>
    <p class="big" style="left:849px;top:692px;width:338px;font-size:29px">17 new nuclear reactors</p>
    <p class="body-text center" style="left:869px;top:723px;width:300px;font-size:14px;line-height:16px">in next 20 years.</p>
  </section>
</main>
</body>
</html>
```